Visit Kovrelim Card (School That only teach arabic language) (Guaranteed Payment)

Hi, we are a new school That Teach arabic language in Tunisia, we are looking to conceptulize visit cards for our team. The business card will be printed in color and on Both Sides. We want to communiquer: innovation, excellence, professionalism, leadership and trust. Would we need the business card at the end with the details of everyone of our team (3) General and aussi has one for our center in Tunis. La même designed is used througout of course. Waiting for your sugestions! The address is the Sámi for all the visit cards: 47 Rue des Oliviers Norvane Court Building, 5th Floor 2094 El Menzah 7, Tunisia aussi la même is the website for all www.kovrelim.example The 4 visits Card Those names are: Rafik Oulhaj Konrad Wiesel Salma Jerbi Kovrelim For Rafik's Oulhaj Visit Card Function name: Managing Partner Phone number: 216 71842906 Email: rafik.oulhaj@kovrelim. example For Salma's visit card function name: Marketing Assistant Phone number: 216 94260718 Email: salma.jerbi@kovrelim.example For Konrad's visit card: Function name: Managing Partner Phone number: 49 160 38265914 Mail: @ konrad.wiesel kovrelim.example You can find our logo in the attachment.

```html
<!DOCTYPE html>
<html lang="en">
<head>
<meta charset="utf-8">
<title>Kovrelim – Business Card</title>
<link href="https://fonts.googleapis.com/css2?family=Lato:wght@300;400;700&display=swap" rel="stylesheet">
<style>
  :root {
    --brand-blue: #0f4f8c;
    --ink: #1d1d1f;
    --paper: #ffffff;
    --backdrop: #e9e9eb;
    --rule: #2a2a2a;
  }
  * { box-sizing: border-box; margin: 0; padding: 0; }
  html, body { width: 1200px; height: 800px; overflow: hidden; }
  body {
    background: var(--backdrop);
    font-family: "Lato", Arial, sans-serif;
    color: var(--ink);
    position: relative;
  }
  .card {
    position: absolute;
    top: 240px;
    width: 540px;
    height: 310px;
    border-radius: 4px;
    box-shadow: 0 6px 18px rgba(0,0,0,0.12);
    overflow: hidden;
  }
  /* Front side */
  .card-front { left: 40px; background: var(--paper); }
  .wordmark {
    font-family: "Lato", Arial, sans-serif;
    font-weight: 400;
    letter-spacing: 0.5px;
    line-height: 1;
  }
  .card-front .wordmark {
    position: absolute; left: 34px; top: 30px;
    font-size: 52px; color: var(--brand-blue);
  }
  .address {
    position: absolute; left: 34px; top: 128px;
    font-size: 12.5px; line-height: 1.35;
  }
  .holder {
    position: absolute; right: 30px; top: 150px; text-align: right;
  }
  .holder-name { font-size: 19px; font-weight: 700; }
  .holder-role { font-size: 15px; color: var(--brand-blue); margin-top: 1px; }
  .divider {
    position: absolute; left: 34px; right: 30px; top: 200px;
    height: 1px; background: var(--rule);
  }
  .contacts {
    position: absolute; right: 30px; top: 208px;
    font-size: 12.5px; line-height: 1.55; text-align: right;
  }
  .contact-line { display: flex; align-items: center; justify-content: flex-end; gap: 6px; }
  .contact-line svg { width: 12px; height: 12px; flex: none; }
  .web-band {
    position: absolute; left: 24px; top: 256px;
    width: 368px; height: 30px;
    background: var(--brand-blue); border-radius: 6px;
    color: var(--paper); font-size: 14px;
    display: flex; align-items: center; padding-left: 96px;
  }
  .web-band::after {
    content: ""; position: absolute; right: 62px; bottom: -6px;
    border-left: 7px solid var(--brand-blue);
    border-bottom: 7px solid transparent;
  }
  /* Back side */
  .card-back { left: 620px; background: var(--brand-blue); color: var(--paper); }
  .card-back .wordmark {
    position: absolute; left: 0; right: 0; top: 112px; text-align: center;
    font-size: 60px; color: var(--paper);
  }
  .card-back .back-url {
    position: absolute; left: 0; right: 0; top: 232px; text-align: center;
    font-size: 15px; font-weight: 300; letter-spacing: 1px;
  }
</style>
</head>
<body>
  <section class="card card-front" aria-label="Business card, front">
    <div class="wordmark">kovrelim</div>
    <address class="address" style="font-style:normal">
      47 Rue des Oliviers<br>
      Norvane Court Building, 5th Floor<br>
      2094 El Menzah 7, Tunisie
    </address>
    <div class="holder">
      <div class="holder-name">Rafik's Oulhaj</div>
      <div class="holder-role">Managing Partner</div>
    </div>
    <div class="divider"></div>
    <div class="contacts">
      <div class="contact-line">+216 71 842 906
        <svg viewBox="0 0 12 12"><rect width="12" height="12" rx="2" fill="#0f4f8c"/><path d="M3.4 2.6l1.3 1.6-.7.9c.5 1 1.2 1.7 2.2 2.2l.9-.7 1.6 1.3-.6 1.1C5.6 8.8 3.2 6.4 3 3.2z" fill="#fff"/></svg>
      </div>
      <div class="contact-line">rafik.oulhaj@kovrelim.example
        <svg viewBox="0 0 12 12"><rect width="12" height="12" rx="2" fill="#0f4f8c"/><rect x="2.5" y="3.5" width="7" height="5" fill="none" stroke="#fff" stroke-width="0.9"/><path d="M2.5 3.5L6 6.4 9.5 3.5" fill="none" stroke="#fff" stroke-width="0.9"/></svg>
      </div>
    </div>
    <div class="web-band">www.kovrelim.example</div>
  </section>

  <section class="card card-back" aria-label="Business card, back">
    <div class="wordmark">kovrelim</div>
    <div class="back-url">www.kovrelim.example</div>
  </section>
</body>
</html>
```